Educational non-profit needs an End of the Year Flyer

We need a flyer to mail to our supporters asking for donations to our program. Crestwood Lantern Youth House runs after school programs for low-income students in Pasadena, CA. This is our end of the year mailing to supporters asking them to finish out the year with their contributions so that we can meet our budget.

Target Market(s)

Donors and supporters of organization

Industry/Entity Type

Non-Profit

Font styles to use
Serif

Colors

Designer to choose colors to be used in the design.

Requirements
Must have
• The project should fit on a 6x9" card, and be printed on front and back. It should show pictures, use the copy I have included, a space for a label address, a stamp, and the return address.
Nice to have
• eye-catching, fun

```html
<!DOCTYPE html>
<html lang="en">
<head>
<meta charset="utf-8">
<title>Crestwood Lantern Youth House – Year End Appeal</title>
<link href="https://fonts.googleapis.com/css2?family=Fira+Sans+Extra+Condensed:ital,wght@0,400;1,500&family=Mountains+of+Christmas:wght@700&family=Permanent+Marker&family=Schoolbell&display=swap" rel="stylesheet">
<style>
  :root {
    --red: #f01414;
    --red-light: #f76a6a;
    --white: #ffffff;
    --ink: #222222;
  }
  html, body { margin: 0; padding: 0; overflow: hidden; }
  body { width: 800px; height: 1200px; }
  .flyer {
    position: relative;
    width: 800px; height: 1200px; overflow: hidden;
    background: linear-gradient(200deg, var(--red-light) 0%, var(--red) 30%, var(--red) 100%);
    color: var(--white);
  }
  .ribbon { position: absolute; inset: 0; }
  .photo { position: absolute; }
  .headline {
    position: absolute; left: 231px; top: 38px; width: 560px; margin: 0;
    font: 400 20px/1 "Permanent Marker", cursive;
    text-transform: uppercase; font-style: italic; white-space: nowrap; overflow: hidden;
  }
  .appeal-line {
    position: absolute; margin: 0; white-space: nowrap;
    font: italic 500 25px/1 "Fira Sans Extra Condensed", sans-serif;
  }
  .greeting {
    position: absolute; left: 440px; width: 350px; top: 762px; margin: 0; text-align: center;
    font: 700 34px/1.1 "Mountains of Christmas", serif; white-space: nowrap;
    text-shadow: 0 0 8px rgba(255,255,255,.7);
  }
  .contacts {
    position: absolute; left: 462px; top: 890px; margin: 0;
    font: 400 17px/26px "Fira Sans Extra Condensed", sans-serif; white-space: nowrap;
  }
  .rule { position: absolute; background: var(--white); }
  .return-address {
    position: absolute; right: 168px; top: 1036px; margin: 0; text-align: right;
    font: 400 17px/25.6px "Schoolbell", cursive; font-style: normal; white-space: nowrap;
  }
  .stamp-box {
    position: absolute; left: 662px; top: 1029px; width: 138px; height: 171px;
    background: var(--white); color: var(--ink);
    display: flex; flex-direction: column; align-items: center; justify-content: center; gap: 12px;
    text-align: center;
  }
  .stamp-box .stamp-spot { width: 54px; height: 62px; border: 2px dashed var(--red); box-sizing: border-box; }
  .stamp-box .name { font: 400 16px/1.15 "Fira Sans Extra Condensed", sans-serif; padding: 0 8px; }
</style>
</head>
<body>
<main class="flyer">
  <svg class="ribbon" width="800" height="1200" viewBox="0 0 800 1200" aria-hidden="true">
    <polygon points="210,43 96,262 333,231" fill="#fff"/>
    <path d="M96,262 C150,250 300,245 389,268 L389,290 L96,275 Z" fill="#f2f2f2"/>
    <polygon points="71,298 389,265 389,428 71,460" fill="#fff"/>
    <path d="M71,460 C150,440 320,432 408,475 L408,490 L71,470 Z" fill="#e9e9e9"/>
    <polygon points="56,505 408,469 408,650 56,682" fill="#fff"/>
    <path d="M56,682 C150,660 330,650 428,695 L428,712 L56,690 Z" fill="#e9e9e9"/>
    <polygon points="36,722 428,690 428,885 36,919" fill="#fff"/>
    <path d="M36,919 C150,895 350,885 447,920 L447,935 L36,925 Z" fill="#e9e9e9"/>
    <polygon points="12,955 447,913 447,1138 12,1175" fill="#fff"/>
  </svg>

  <svg class="photo" style="left:0;top:0" width="400" height="300" role="img" aria-label="Photo of a smiling young girl on the playground">
    <defs><linearGradient id="g1" x1="0" y1="0" x2="1" y2="1"><stop offset="0" stop-color="#9c8a72"/><stop offset="1" stop-color="#5a4b44"/></linearGradient></defs>
    <polygon points="204,68 126,238 305,222" fill="url(#g1)"/>
  </svg>
  <div class="photo" role="img" aria-label="Photo of students performing on stage at a holiday concert" style="left:80px;top:301px;width:187px;height:134px;background:linear-gradient(180deg,#2a2220,#6a4a3c 60%,#c05050)"></div>
  <div class="photo" role="img" aria-label="Photo of children on a tire swing" style="left:279px;top:293px;width:99px;height:122px;background:linear-gradient(180deg,#6f8a62,#a89a88)"></div>
  <div class="photo" role="img" aria-label="Photo of two sisters hugging" style="left:70px;top:503px;width:135px;height:165px;background:linear-gradient(160deg,#2a2424,#7a4a5a)"></div>
  <div class="photo" role="img" aria-label="Photo of students playing guitars on stage" style="left:214px;top:481px;width:184px;height:167px;background:linear-gradient(180deg,#8a6a55,#b08868 70%,#ddd)"></div>
  <div class="photo" role="img" aria-label="Photo of a student holding a handwritten letter in class" style="left:52px;top:719px;width:129px;height:185px;background:linear-gradient(180deg,#c9b47a,#6a5a52)"></div>
  <div class="photo" role="img" aria-label="Photo of girls with basketballs in the gym" style="left:196px;top:700px;width:215px;height:182px;background:linear-gradient(180deg,#b9a07e,#4a3a3a)"></div>
  <div class="photo" role="img" aria-label="Group photo of kids club members in the gym" style="left:34px;top:956px;width:238px;height:204px;background:linear-gradient(180deg,#a89678,#3e3840)"></div>
  <div class="photo" role="img" aria-label="Photo of children preparing trays of food" style="left:289px;top:941px;width:131px;height:188px;background:linear-gradient(160deg,#5a4a44,#c8c8a8 60%,#a83030)"></div>

  <h1 class="headline">We need your help to finish out 2018 strong!</h1>

  <section class="appeal">
    <p class="appeal-line" style="left:321px;top:84px">We have had a wonderful 25th year of</p>
    <p class="appeal-line" style="left:324px;top:128px">serving the children and families of Pasadena</p>
    <p class="appeal-line" style="left:352px;top:172px">here at Crestwood Lantern Youth House</p>
    <p class="appeal-line" style="left:370px;top:216px">with high quality afterschool programs.</p>
    <p class="appeal-line" style="left:420px;top:261px">Hundreds and hundreds of students</p>
    <p class="appeal-line" style="left:424px;top:305px">have been a part of</p>
    <p class="appeal-line" style="left:420px;top:349px">the Lantern Kids Club family.</p>
    <p class="appeal-line" style="left:420px;top:394px">Our annual budget is $275,000 and</p>
    <p class="appeal-line" style="left:434px;top:438px">we count on $100,000 from</p>
    <p class="appeal-line" style="left:438px;top:482px">individual donors.</p>
    <p class="appeal-line" style="left:438px;top:527px">Will you join with us for an end of</p>
    <p class="appeal-line" style="left:438px;top:571px">the year contribution? Remember,</p>
    <p class="appeal-line" style="left:433px;top:616px">you can give online through GiveLink.</p>
    <p class="appeal-line" style="left:455px;top:661px">Just look for the link on our</p>
    <p class="appeal-line" style="left:452px;top:705px">website - www.lanternkids.org.</p>
  </section>

  <p class="greeting">Merry Christmas<br>from all of us at CLYH!</p>

  <p class="contacts">
    Website - www.lanternkids.org<br>
    Facebook - Crestwood Lantern Youth House<br>
    Email:&nbsp; hello@lanternkids.org
  </p>

  <div class="rule" style="left:649px;top:981px;width:2px;height:219px"></div>
  <div class="rule" style="left:568px;top:1018px;width:232px;height:2px"></div>

  <address class="return-address">
    Crestwood Lantern<br>
    Youth House<br>
    214 N.<br>
    Alder Ave.<br>
    Pasadena, CA&nbsp; 91106<br>
    (626) 555-0142
  </address>

  <div class="stamp-box">
    <span class="stamp-spot" aria-label="Stamp area" role="img"></span>
    <span class="name">Crestwood Lantern Youth House</span>
  </div>
</main>
</body>
</html>
```